Re-design of veterinary clinic website *

For a future relaunch of our webpage, we would like to find a fresh design that still incorporates the spirit of our current one which can be found at http://dr-wenzlaff.de
We are a small business that appeals to locals but are known in a wide area for specialist services.
According to analytics data, most people rarely read through the full website but are using it to inform themselves about opening hours, Telephone numbers and location. Still, the website needs to offer enough content to be ranked positively by the Quandle algorithm.
Our logo is not part of the re-design but needs to be included in your proposal as is. It can be used a source of inspiration, just as the current design. Keep in mind, that the design will be used as the basis of a fluid webdesign for both mobile and desktop. Roughly 75% of our users are on mobile devices.
Target Market(s)
Locals
Industry/Entity Type
Veterinary
Number of Pages Required
1 page
Look and feel
Each slider illustrates characteristics of the customer's brand and the style your logo design should communicate.

```html
<!DOCTYPE html>
<html lang="de">
<head>
<meta charset="utf-8">
<title>Tierarztpraxis Dr. med. vet. Harald Wenzlaff</title>
<link href="https://fonts.googleapis.com/css2?family=PT+Sans:wght@400;700&display=swap" rel="stylesheet">
<style>
:root{
  --blue:#0b4f9e;
  --blue-dark:#083f80;
  --sky:#8ecbe7;
  --sky-light:#bfe2f2;
  --ice:#eef5fa;
  --text:#333a44;
  --muted:#6b7480;
  --white:#ffffff;
  --line:#d9e1e8;
}
*{box-sizing:border-box;margin:0;padding:0}
html,body{width:1200px;height:3364px;overflow:hidden}
body{font-family:"PT Sans",Arial,sans-serif;color:var(--text);background:var(--white);font-size:13px;line-height:1.55;position:relative}
section,header,footer{position:absolute;left:0;width:1200px}
.container{position:absolute;left:36px;width:1128px}
h2{font-weight:700}

/* header */
.site-header{top:0;height:130px;background:var(--white)}
.brand{position:absolute;left:161px;top:14px;display:flex;align-items:center;gap:14px}
.brand-mark{width:18px;height:18px;border-radius:50%;background:var(--blue)}
.brand-name{font-size:24px;font-weight:700;color:var(--blue);letter-spacing:1px}
.brand-sub{position:absolute;left:161px;top:54px;font-size:12px;color:var(--blue)}
.btn-appoint{position:absolute;left:879px;top:30px;width:160px;height:30px;background:var(--sky);color:var(--white);font-size:12px;display:flex;align-items:center;justify-content:center;border-radius:2px}
.main-nav{position:absolute;left:161px;top:96px;width:878px;height:34px;display:flex;border-bottom:2px solid var(--blue)}
.main-nav a{flex:1;display:flex;align-items:center;justify-content:center;font-size:12px;font-weight:700;color:var(--blue);text-decoration:none;border-right:1px solid var(--line)}
.main-nav a.active{background:var(--blue);color:var(--white)}

/* hero */
.hero{top:130px;height:450px;background:linear-gradient(180deg,var(--sky) 0%,#a4d5ec 70%,var(--white) 100%)}
.hero-title{position:absolute;left:161px;top:132px;width:480px;font-size:27px;line-height:1.3;color:var(--white)}
.hero-text{position:absolute;left:161px;top:215px;width:480px;font-size:12px;color:var(--white)}
.hero-btn{position:absolute;left:161px;top:283px;width:158px;height:30px;background:var(--white);color:var(--blue);font-size:12px;display:flex;align-items:center;justify-content:center;border-radius:2px}
.hero-pets{position:absolute;left:600px;top:40px;width:460px;height:410px;border-radius:46% 46% 8px 8px;background:radial-gradient(ellipse at 40% 55%,#b08660 0%,#d8b47f 40%,rgba(230,210,170,0) 70%)}

/* hours + contact */
.info{top:583px;height:303px}
.hours{position:absolute;left:36px;top:0;width:565px;height:303px;background:var(--blue);color:var(--white);padding:22px 30px}
.hours h2{font-size:16px;text-transform:uppercase;margin-bottom:12px}
.hours-row{display:grid;grid-template-columns:190px 150px 150px;font-size:11px;height:38px;align-items:center;border-bottom:1px solid rgba(255,255,255,.25)}
.hours-row b{font-weight:700}
.hours-row span{text-align:center}
.hours-row span+span{border-left:1px solid rgba(255,255,255,.4)}
.contact-card{position:absolute;left:601px;top:0;width:561px;height:303px;background:var(--white);box-shadow:0 4px 18px rgba(0,0,0,.12);text-align:center;padding-top:40px}
.contact-card h2{font-size:26px;font-weight:400;color:var(--blue)}
.contact-card h3{font-size:16px;margin-top:8px}
.contact-card .sub{font-size:11px;color:var(--muted);margin-top:10px}
.contact-card .addr{font-size:12px;margin-top:24px;display:flex;justify-content:center;gap:8px;align-items:center}
.phones{display:flex;justify-content:center;gap:50px;margin-top:30px;font-size:12px}
.phones div{display:flex;align-items:center;gap:8px}
.phones b{color:var(--blue)}
.icon-ring{width:30px;height:30px;border:1px solid var(--line);border-radius:50%;display:flex;align-items:center;justify-content:center}

/* welcome */
.welcome{top:942px;height:390px}
.welcome h2{position:absolute;left:36px;top:0;font-size:26px;color:var(--blue)}
.welcome h3{position:absolute;left:36px;top:45px;font-size:17px}
.welcome-text{position:absolute;left:36px;top:78px;width:555px;font-size:11px;color:var(--muted)}
.welcome-text p{margin-bottom:11px}
.btn-more{position:absolute;left:36px;top:340px;width:106px;height:30px;background:var(--blue);color:var(--white);font-size:11px;display:flex;align-items:center;justify-content:center;border-radius:2px}
.photo{position:absolute}
.photo-a{left:610px;top:7px;width:272px;height:360px;background:linear-gradient(160deg,#9a8a72,#c9b48f 55%,#7c6b55)}
.photo-b{left:893px;top:7px;width:270px;height:172px;background:linear-gradient(180deg,#5f7f5c,#dfe4e6 55%,#9aa3a6)}
.photo-c{left:893px;top:193px;width:270px;height:174px;background:linear-gradient(180deg,#e9eef2,#7aa36c 60%,#4f6f45)}

/* services */
.services-band{top:1373px;height:163px;background:var(--blue);color:var(--white);text-align:center}
.services-band h2{font-size:24px;font-weight:400;margin-top:40px}
.services-band p{font-size:12px;width:560px;margin:10px auto 0;line-height:1.5}
.band-arrow{position:absolute;left:584px;bottom:-14px;width:0;height:0;border-left:16px solid transparent;border-right:16px solid transparent;border-top:14px solid var(--blue)}
.services{top:1581px;height:440px}
.svc{position:absolute;width:400px}
.svc h3{font-size:16px;color:var(--blue);margin-bottom:14px}
.svc p{font-size:11px;color:var(--muted);line-height:1.55}
.svc .more{font-size:11px;font-weight:700;color:var(--text);margin-top:6px}
.svc-icon{position:absolute;top:-8px;width:50px;height:50px;border-radius:50%;background:var(--sky);display:flex;align-items:center;justify-content:center}
.svc-left{left:36px;text-align:right}
.svc-left h3{padding-right:60px}
.svc-left .svc-icon{right:0}
.svc-right{left:761px}
.svc-right h3{padding-left:62px}
.svc-right .svc-icon{left:0}
.svc-photo{position:absolute;left:460px;top:10px;width:280px;height:420px;border:3px solid var(--sky-light);box-shadow:0 4px 16px rgba(0,0,0,.12);background:linear-gradient(180deg,#f4f7f9 0%,#3c6fb8 45%,#e9e3da 75%,#c99a6a 100%)}

/* team */
.team{top:2064px;height:460px;background:var(--sky)}
.team h2{text-align:center;font-size:24px;font-weight:400;color:var(--white);margin-top:52px}
.team-grid{position:absolute;left:38px;top:124px;display:flex;gap:16px}
.member{width:175px;height:250px;background:var(--white);padding:7px;position:relative}
.member-photo{width:161px;height:236px;background:linear-gradient(180deg,#b7c1c9,#8c9aa6 55%,#5b6a78)}
.member-name{position:absolute;left:7px;right:7px;bottom:7px;height:36px;background:var(--blue);color:var(--white);font-size:14px;font-weight:700;display:flex;align-items:center;justify-content:center}
.member.featured .member-name{top:90px;bottom:auto;height:96px;flex-direction:column;background:rgba(11,79,158,.9)}
.member.featured .member-photo{height:196px}
.details{margin-top:10px;border:1px solid var(--white);font-size:11px;font-weight:400;padding:3px 14px}
.member-social{position:absolute;left:0;right:0;bottom:12px;display:flex;justify-content:center;gap:12px}
.member-social i{width:22px;height:22px;border-radius:50%;background:var(--sky)}
.dots{position:absolute;left:582px;top:394px;display:flex;gap:6px}
.dots i{width:7px;height:7px;border-radius:50%;background:var(--sky-light);border:1px solid var(--white)}
.dots i.on{background:var(--white)}

/* contact form */
.contact{top:2524px;height:464px}
.contact h2{position:absolute;left:36px;top:0;font-size:26px;color:var(--blue)}
.contact .intro{position:absolute;left:36px;top:40px;width:360px;font-size:11px;color:var(--muted)}
.form{position:absolute;left:38px;top:82px;width:550px}
.field{height:30px;background:var(--ice);border:1px solid var(--line);font-size:11px;color:var(--muted);display:flex;align-items:center;padding-left:12px;margin-bottom:12px}
.pair{display:flex;gap:12px}
.pair .field{flex:1}
.field.msg{height:74px;align-items:flex-start;padding-top:8px}
.btn-submit{width:82px;height:30px;background:var(--blue);color:var(--white);font-size:11px;font-weight:700;display:flex;align-items:center;justify-content:center;border-radius:2px;margin-top:8px}
.circle{position:absolute;left:648px;top:58px;width:370px;height:370px;border-radius:50%;background:var(--blue);color:var(--white);text-align:center}
.circle .pin{width:46px;height:46px;border-radius:50%;background:rgba(255,255,255,.2);margin:32px auto 0;display:flex;align-items:center;justify-content:center}
.circle .city{font-size:14px;margin-top:14px}
.circle .rule{width:250px;height:1px;background:rgba(255,255,255,.3);margin:16px auto}
.circle .note{width:250px;margin:0 auto;font-size:11px;line-height:1.5}
.circle .tel{display:flex;justify-content:center;align-items:center;gap:12px;margin-top:30px;font-size:15px;text-align:left}
.circle .tel b{font-size:18px}
.dogs{position:absolute;left:940px;top:230px;width:262px;height:240px;border-radius:50% 50% 0 0;background:radial-gradient(ellipse at 50% 70%,#8a5a33 0%,#c08a55 40%,rgba(255,255,255,0) 72%)}

/* footer */
.site-footer{top:2988px;height:376px;background:var(--blue);color:var(--white)}
.footer-cols{position:absolute;left:161px;top:54px;display:flex;gap:30px}
.footer-cols h4{font-size:13px;text-transform:uppercase;margin-bottom:18px}
.footer-cols p,.footer-cols li{font-size:10.5px;line-height:1.65;list-style:none}
.col-about{width:270px}
.col-links{width:120px}
.col-links li,.col-services li{margin-bottom:6px}
.col-services{width:200px}
.col-news{width:210px}
.subscribe{margin-top:12px;height:28px;border:1px solid rgba(255,255,255,.6);font-size:10.5px;display:flex;align-items:center;padding-left:10px}
.btn-send{margin-top:14px;width:74px;height:28px;background:var(--white);color:var(--blue);font-size:11px;font-weight:700;display:flex;align-items:center;justify-content:center}
.footer-bottom{position:absolute;left:0;top:332px;width:1200px;height:44px;border-top:1px solid rgba(255,255,255,.25);font-size:10.5px;padding:14px 161px}
</style>
</head>
<body>

<header class="site-header">
  <div class="brand"><span class="brand-mark"></span><span class="brand-name">Harald Wenzlaff</span></div>
  <div class="brand-sub">Dr. med. vet. · Fachtierarzt für Kleintiere</div>
  <div class="btn-appoint">Request An Appointment</div>
  <nav class="main-nav">
    <a class="active">HAUPTSEITE</a><a>PRAXIS</a><a>TEAM</a><a>SPRECHZEITEN</a><a>LEISTUNGEN</a><a style="border-right:0">KONTAKT / ANFAHRT</a>
  </nav>
</header>

<section class="hero">
  <h1 class="hero-title">Persönliche Betreuung Ihrer Haustiere in den eigenen vier Wänden</h1>
  <p class="hero-text">Herzlich Willkommen auf der Homepage der Tierarztpraxis von Dr. Harald Wenzlaff. Mein Team und ich haben hier Informationen rund um die Praxis und Hinweise für Patientenbesitzer zusammengestellt.</p>
  <div class="hero-btn">Unsere Dienstleistungen</div>
  <div class="hero-pets" role="img" aria-label="Foto einer Katze und eines Hundes nebeneinander"></div>
</section>

<section class="info">
  <div class="hours">
    <h2>Sprechzeiten ohne Terminvereinbarung</h2>
    <div class="hours-row"><b>Montag</b><span>9:30 AM - 11:00 AM</span><span>16:00 PM - 19:00 PM</span></div>
    <div class="hours-row"><b>Dienstag</b><span>9:30 AM - 11:00 AM</span><span>16:00 PM - 19:00 PM</span></div>
    <div class="hours-row"><b>Mittwoch</b><span>9:30 AM - 11:00 AM</span><span>16:00 PM - 19:00 PM</span></div>
    <div class="hours-row"><b>Donnerstag</b><span>———————</span><span>16:00 PM - 19:00 PM</span></div>
    <div class="hours-row"><b>Freitag</b><span>9:30 AM - 11:00 AM</span><span>16:00 PM - 19:00 PM</span></div>
    <div class="hours-row" style="border-bottom:0"><b>Samstag</b><span>9:30 AM - 11:00 AM</span><span>———————</span></div>
  </div>
  <div class="contact-card">
    <h2>Kontakt</h2>
    <h3>Dr. med. vet. Harald Wenzlaff</h3>
    <p class="sub">Fachtierarzt für Kleintiere Lindenweg 4</p>
    <p class="addr"><svg width="14" height="16" viewBox="0 0 14 16"><path d="M7 1a5 5 0 0 1 5 5c0 4-5 9-5 9S2 10 2 6a5 5 0 0 1 5-5z" fill="none" stroke="#0b4f9e" stroke-width="1.5"/><circle cx="7" cy="6" r="1.8" fill="#0b4f9e"/></svg>14167 Berlin (Lichterfelde)</p>
    <div class="phones">
      <div><span class="icon-ring"><svg width="14" height="14" viewBox="0 0 14 14"><path d="M3 1l2 3-1.3 1.3a8 8 0 0 0 5 5L10 9l3 2-1.5 2C6 13 1 8 1 2.5z" fill="#0b4f9e"/></svg></span>Telefon: <b>030 / 555 01 23</b></div>
      <div><span class="icon-ring"><svg width="14" height="14" viewBox="0 0 14 14"><path d="M3 1l2 3-1.3 1.3a8 8 0 0 0 5 5L10 9l3 2-1.5 2C6 13 1 8 1 2.5z" fill="#0b4f9e"/></svg></span>Telefax: <b>030 / 555 01 24</b></div>
    </div>
  </div>
</section>

<section class="welcome">
  <h2>Herzlich Willkommen!</h2>
  <h3>Praxis</h3>
  <div class="welcome-text">
    <p>Meine Kleintierpraxis befindet sich im Lindenweg, die direkt an der S-Bahnlinie S1 entlangführt, etwa 50 Meter vom S-Bahnhof Lichterfelde entfernt.</p>
    <p>Ich habe die Praxis 1985 gegründet. Die Praxisräume befanden sich zuerst im Lindenweg 1. 1995 sind wir in die jetzigen, grösseren Räume im Lindenweg 4 umgezogen.</p>
    <p>Die Praxis verfügt auf 190 qm Fläche unter anderem über zwei Behandlungsräume, einen Röntgenraum, einen Operationsvorbereitungs- und Aufwachbereich und einen OP.</p>
    <p>Die Behandlungsräume und das Wartezimmer sind klimatisiert. Den Anmeldungs- und Verkaufsbereich ist in das grosszügige Wartezimmer integriert, in dem wir die Wartezeit mit Zeitschriften und Erfrischungsgetränken verkürzen möchten. So haben Sie bei Fragen und Problemen immer einen direkten Ansprechpartner, und wenn Sie nur etwas abholen möchten, kann Ihnen ebenfalls rasch weitergeholfen werden.</p>
  </div>
  <div class="btn-more">▸ Weiterlesen</div>
  <div class="photo photo-a" role="img" aria-label="Foto des Wartezimmers der Praxis"></div>
  <div class="photo photo-b" role="img" aria-label="Foto des Praxiseingangs"></div>
  <div class="photo photo-c" role="img" aria-label="Foto des Praxisgebäudes mit Garten"></div>
</section>

<section class="services-band">
  <h2>Unsere Dienstleistungen</h2>
  <p>Lorem ipsum dolor sitzen amet, consectetur adipiscing elit, sed do eiusmod temporary incididunt ut labore und dolore magna aliqua. Ut enim ad minim veniam, quis nostrud ausübung ullamco laboris nisi ut</p>
  <span class="band-arrow"></span>
</section>

<section class="services">
  <div class="svc svc-left" style="top:12px"><span class="svc-icon"><svg width="24" height="24" viewBox="0 0 24 24" fill="#fff"><circle cx="12" cy="15" r="5"/><circle cx="5" cy="9" r="2.3"/><circle cx="19" cy="9" r="2.3"/><circle cx="9" cy="4.5" r="2.3"/><circle cx="15" cy="4.5" r="2.3"/></svg></span><h3>Hunden</h3><p><b style="color:var(--text)">Welpenbetreuung:</b> Sie möchten mit einem oder mehreren Hunden Ihr Leben teilen ....bereits? Dann können wir als Tierärzte viel oder tun dies</p><div class="more">Read More</div></div>
  <div class="svc svc-left" style="top:162px"><span class="svc-icon"><svg width="24" height="24" viewBox="0 0 24 24" fill="#fff"><circle cx="12" cy="15" r="5"/><circle cx="5" cy="9" r="2.3"/><circle cx="19" cy="9" r="2.3"/><circle cx="9" cy="4.5" r="2.3"/><circle cx="15" cy="4.5" r="2.3"/></svg></span><h3>Katzen</h3><p>Wir möchten zusammen mit Ihnen Ihrer Katze ein gesundes, langes Leben ...... ermöglichen, und bieten Ihnen daher unter anderem</p><div class="more">Read More</div></div>
  <div class="svc svc-left" style="top:312px"><span class="svc-icon"><svg width="24" height="24" viewBox="0 0 24 24" fill="#fff"><circle cx="12" cy="15" r="5"/><circle cx="5" cy="9" r="2.3"/><circle cx="19" cy="9" r="2.3"/><circle cx="9" cy="4.5" r="2.3"/><circle cx="15" cy="4.5" r="2.3"/></svg></span><h3>Kleinsäugern</h3><p>In die Kategorie "Kleinsäuger" fallen viele in ihren Bedürfnissen sehr Anspruchsvolle ...... Meerschweinchen, unterschiedliche Tierarten</p><div class="more">Read More</div></div>

  <div class="svc-photo" role="img" aria-label="Foto einer Tierärztin mit einem weissen Hund"></div>

  <div class="svc svc-right" style="top:12px"><span class="svc-icon"><svg width="22" height="22" viewBox="0 0 22 22" fill="none" stroke="#fff" stroke-width="2"><rect x="4" y="3" width="14" height="17" rx="2"/><path d="M8 9h6M11 6v6M8 16h6"/></svg></span><h3>Behandlungsschwerpunkten</h3><p>Unsere Behandlungsschwerpunkte liegen in der Inneren Medizin und Chirurgie der Hunde und Katzen. Dabei möchten wir folgende Punkte ...</p><div class="more">Read More</div></div>
  <div class="svc svc-right" style="top:162px"><span class="svc-icon"><svg width="22" height="22" viewBox="0 0 22 22" fill="none" stroke="#fff" stroke-width="2"><rect x="4" y="3" width="14" height="17" rx="2"/><path d="M8 9h6M11 6v6M8 16h6"/></svg></span><h3>Behandlungsschwerpunkte</h3><p>Die Praxis bietet folgende besondere Betreuungs- und Beratungsleistungen:<br>● Beratung und Betreuung vor Auslandsreisen, auch nach...</p><div class="more">Read More</div></div>
  <div class="svc svc-right" style="top:312px"><span class="svc-icon"><svg width="22" height="22" viewBox="0 0 22 22" fill="none" stroke="#fff" stroke-width="2"><rect x="4" y="3" width="14" height="17" rx="2"/><path d="M8 9h6M11 6v6M8 16h6"/></svg></span><h3>Medizinische Einrichtungen</h3><p>Die Praxis verfügt unter anderem über folgende medizinische Einrichtungen zur Untersuchung und Behandlung:</p><div class="more">Read More</div></div>
</section>

<section class="team">
  <h2>Unser Team</h2>
  <div class="team-grid">
    <div class="member featured"><div class="member-photo" role="img" aria-label="Porträtfoto Dr. Harald Wenzlaff"></div><div class="member-name">Dr. Harald Wenzlaff<span class="details">View Details</span></div><div class="member-social"><i></i><i></i><i></i><i></i></div></div>
    <div class="member"><div class="member-photo" role="img" aria-label="Porträtfoto Lena Ostermann"></div><div class="member-name">Lena Ostermann</div></div>
    <div class="member"><div class="member-photo" role="img" aria-label="Porträtfoto Mara Lindqvist mit Katze"></div><div class="member-name">Mara Lindqvist</div></div>
    <div class="member"><div class="member-photo" role="img" aria-label="Porträtfoto Jana Kessler"></div><div class="member-name">Jana Kessler</div></div>
    <div class="member"><div class="member-photo" role="img" aria-label="Porträtfoto Dr. Ute Falkenberg"></div><div class="member-name">Dr. Ute Falkenberg</div></div>
    <div class="member"><div class="member-photo" role="img" aria-label="Porträtfoto Nina Hartwig"></div><div class="member-name">Nina Hartwig</div></div>
  </div>
  <div class="dots"><i class="on"></i><i></i><i></i></div>
</section>

<section class="contact">
  <h2>In Kontakt kommen</h2>
  <p class="intro">Bitte füllen Sie dieses Formular aus und senden Sie es ab. Ein Mitarbeiter unseres Teams wird umgehend antworten</p>
  <div class="form">
    <div class="field">👤 Your Name</div>
    <div class="pair"><div class="field">✉ Email</div><div class="field">☏ Phone</div></div>
    <div class="pair"><div class="field">⚙ Service</div><div class="field">▦ Date</div></div>
    <div class="field msg">? Message</div>
    <div class="btn-submit">SUBMIT</div>
  </div>
  <div class="circle">
    <div class="pin"><svg width="18" height="22" viewBox="0 0 14 16"><path d="M7 1a5 5 0 0 1 5 5c0 4-5 9-5 9S2 10 2 6a5 5 0 0 1 5-5z" fill="#fff"/><circle cx="7" cy="6" r="1.8" fill="#0b4f9e"/></svg></div>
    <p class="city">14167 Berlin (Lichterfelde)</p>
    <div class="rule"></div>
    <p class="note">Also at night, on weekends and on public holidays, we try in urgent emergencies under our practice phone number 0170 555 019 9 to be available for you.</p>
    <div class="tel"><span class="icon-ring" style="background:#fff;border:0;width:42px;height:42px"><svg width="18" height="18" viewBox="0 0 14 14"><path d="M3 1l2 3-1.3 1.3a8 8 0 0 0 5 5L10 9l3 2-1.5 2C6 13 1 8 1 2.5z" fill="#0b4f9e"/></svg></span><div>Telefon: <b>030 / 555 01 23</b><br>Telefax: <b>030 / 555 01 24</b></div></div>
  </div>
  <div class="dogs" role="img" aria-label="Foto einer Gruppe kleiner Hunde"></div>
</section>

<footer class="site-footer">
  <div class="footer-cols">
    <div class="col-about"><h4>Über uns</h4><p>Meine Kleintierpraxis befindet sich im Lindenweg, die direkt an der S-Bahnlinie S1 entlangführt, etwa 50 Meter vom S-Bahnhof Lichterfelde entfernt.</p><p style="margin-top:10px">Ich habe die Praxis 1985 gegründet. Die Praxisräume befanden sich zuerst im Lindenweg 1. 1995 sind wir in die jetzigen, grösseren Räume im Lindenweg 4 umgezogen.</p><p style="margin-top:10px;font-weight:700">Read More</p></div>
    <div class="col-links"><h4>Quick Links</h4><ul><li style="text-decoration:underline">Hauptseite</li><li>Praxis</li><li>Team</li><li>Sprechzeiten</li><li>Leistungen</li><li>Kontakt / Anfahrt</li></ul></div>
    <div class="col-services"><h4>Unsere Dienstleistungen</h4><ul><li>Hunden</li><li>Katzen</li><li>Kleinsäugern</li><li>Behandlungsschwerpunkten</li><li>besondere Beratungs- und Betreuungsleistungen</li><li>Technischer Einrichtungen zur Untersuchung und Behandlung</li><li>Cloud Security</li></ul></div>
    <div class="col-news"><h4>Abonnieren Sie uns</h4><p>Abonniere unseren Newsletter! um die neuesten Nachrichten und Updates zu Pet Care</p><div class="subscribe">✉ Your email Address</div><div class="btn-send">SEND</div></div>
  </div>
  <div class="footer-bottom">© 2018 Dr. med. vet. Harald Wenzlaff All rights reserved.</div>
</footer>

</body>
</html>
```